Packaging Design for Peach Halves in Syrup

Hello Designer,
We have to create a packaging design for a peach halves in syrup product.
The design should be eye-catching, appealing to the target europeen market, and convey the product's quality and freshness.
Peach halves in syrup, packed in glass jars with yellow lids. The jar size is as a picture attached below.
Logo : MOLAN
Label Design: Design a label that prominently features the product name in english and french, "Peach Halves in Syrup," "Pêches en moitiés" and highlights key selling points such as "100% Natural" or "No Added Preservatives."
Visual Elements: Incorporate image or illustration of ripe peaches to emphasize the product's freshness and natural ingredients.
Color Scheme: Use a color scheme that complements the yellow lids, making the product stand out on the shelf. Consider using warm, inviting colors to evoke the feeling of freshness.

Nutritional Information: Include a panel for nutritional information.
ingredients list -Eng : peaches, water, Sugar.
-Fr : pêches, eau, sucre.
Barcode: leave a space for barcode.

Target Market(s)

Europe

Font styles to use
Serif
Decorative
Script

Requirements
Must have
• -Product name : ENG and FR, barcode, nutritional information, ingredients : Eng and French.

```html
<!DOCTYPE html>
<html lang="en">
<head>
<meta charset="UTF-8">
<title>MOLAN Peach Halves in Syrup – Jar Label</title>
<link href="https://fonts.googleapis.com/css2?family=Playfair+Display:wght@400;700&family=Great+Vibes&display=swap" rel="stylesheet">
<style>
  :root {
    --amber: #F5AC1F;
    --magenta: #C4096F;
    --tangerine: #EE7F1A;
    --placeholder-grey: #D9D9D9;
    --white: #FFFFFF;
    --peach-red: #C8322C;
    --peach-gold: #F2A93B;
    --leaf: #3E8E3A;
  }
  * { box-sizing: border-box; margin: 0; padding: 0; }
  html, body {
    width: 1200px; height: 1200px; overflow: hidden;
    background: var(--white);
  }
  .canvas { position: relative; width: 1200px; height: 1200px; }

  .jar-label {
    position: absolute; left: 40px; top: 425px;
    width: 1120px; height: 350px;
    background: var(--magenta);
    font-family: "Playfair Display", Georgia, serif;
    color: var(--white);
    overflow: hidden;
  }
  .top-band {
    position: absolute; left: 0; top: 0; width: 100%; height: 85px;
    background: var(--amber);
    z-index: 0;
  }
  .brand-name {
    position: absolute; left: 0; width: 100%; top: 36px; height: 66px;
    z-index: 2;
    text-align: center;
    font-family: "Playfair Display", Georgia, serif;
    font-weight: 700; font-size: 48px; letter-spacing: 2px;
    line-height: 66px;
    color: var(--white);
  }

  .nutrition-caption {
    position: absolute; left: 27px; top: 108px;
    font-size: 13px; line-height: 1.2;
  }
  .nutrition-panel {
    position: absolute; left: 34px; top: 148px;
    width: 182px; height: 157px;
    background: var(--placeholder-grey);
  }

  .product-title {
    position: absolute; left: 393px; top: 130px;
    font-size: 42px; font-weight: 400; line-height: 1.1; white-space: nowrap;
  }
  .product-title .in-syrup {
    font-family: "Great Vibes", "Brush Script MT", cursive;
    font-size: 28px; margin-left: 6px;
  }
  .french-name-pill {
    position: absolute; left: 407px; top: 185px;
    width: 308px; height: 33px; border-radius: 9px;
    background: var(--tangerine);
  }
  .french-name {
    position: absolute; left: 407px; top: 183px; width: 308px; height: 36px;
    text-align: center; font-size: 28px; line-height: 36px; white-space: nowrap;
  }

  .peach-illustration {
    position: absolute; left: 448px; top: 224px;
    width: 245px; height: 112px; border-radius: 56px 40px 50px 50px;
    background: radial-gradient(ellipse at 35% 60%, var(--peach-red) 0%, var(--peach-gold) 55%, rgba(62,142,58,0.75) 100%);
  }

  .claim-preservatives {
    position: absolute; left: 348px; top: 266px;
    text-transform: uppercase; line-height: 0.95;
  }
  .claim-preservatives .claim-no { display: block; font-size: 27px; padding-left: 6px; }
  .claim-preservatives .claim-added { display: block; font-size: 29px; }
  .claim-preservatives .claim-small { display: block; font-size: 11px; line-height: 1.3; }

  .natural-badge {
    position: absolute; left: 700px; top: 222px;
    width: 70px; height: 70px;
  }

  .ingredients {
    position: absolute; left: 909px; top: 95px;
    font-size: 13px; line-height: 16px;
  }
  .ingredients p + p { margin-top: 16px; }

  .barcode-space {
    position: absolute; left: 903px; top: 246px;
    width: 177px; height: 75px;
    background: var(--placeholder-grey);
  }
</style>
</head>
<body>
<main class="canvas">
  <section class="jar-label" aria-label="Peach halves in syrup jar label">
    <div class="top-band"></div>
    <div class="brand-name">MOLAN</div>

    <p class="nutrition-caption">panel for nutritional information</p>
    <div class="nutrition-panel"></div>

    <h1 class="product-title">Peach Halves<span class="in-syrup">in Syrup</span></h1>
    <div class="french-name-pill"></div>
    <p class="french-name">Pêches en moitiés</p>

    <div class="peach-illustration" role="img" aria-label="Illustration of ripe whole and halved peaches with green leaves"></div>

    <p class="claim-preservatives">
      <span class="claim-no">No</span>
      <span class="claim-added">Added</span>
      <span class="claim-small">Preservatives</span>
    </p>

    <svg class="natural-badge" viewBox="0 0 74 74" aria-label="100% Natural">
      <defs>
        <path id="badge-arc" d="M37,37 m-28,0 a28,28 0 1,1 56,0 a28,28 0 1,1 -56,0"/>
      </defs>
      <text font-family="Playfair Display, Georgia, serif" font-size="10" fill="#FFFFFF" letter-spacing="3">
        <textPath href="#badge-arc" startOffset="8%">100% NATURAL</textPath>
      </text>
      <circle cx="37" cy="37" r="15" fill="none" stroke="#FFFFFF" stroke-width="1.3"/>
      <path d="M37 27 C45 32 45 42 37 47 C29 42 29 32 37 27 Z" fill="#FFFFFF"/>
      <path d="M37 31 V46 M37 38 L41 35 M37 42 L33 39" stroke="#C4096F" stroke-width="1" fill="none"/>
    </svg>

    <div class="ingredients">
      <p>ingredients list<br>peaches, water, Sugar.</p>
      <p>liste des ingrédients<br>pêches, eau, sucre.</p>
    </div>

    <div class="barcode-space"></div>
  </section>
</main>
</body>
</html>
```